Strata Edge Supply Business Card Design Challenge

Please create me a simple card using my logo. I'm not looking for anything abstract.
A couple of colours for text and maybe something on the card so the whole card isn't just a white board.
Please send me samples and I'll reply with suggestions to refine the design. Thank you

Reason: The Ormeau address was incorrect in the brief, so I have updated that so the 4 and 5 star submissions can be updated and resubmitted please!!! Sorry and thank you

Target Market(s)

Mining companies and rock producing aggregate companies. Quarries

Industry/Entity Type

Mining

Contact Information for Business Card

Name - Lewis Trenholm / Company Logo AND Strata Edge Supply Pty Ltd / position - Managing Director / address1 - Unit 3, 14 Kestrel Parade, Ormeau 4208 Queensland AU / address2 - PO Box 917, Oxenford 4210 Queensland AU / mobile - 0427 195 864 / phone - 07 5571 9346 / fax - 07 5571 9420 / email - lt@strataedgesupply.example.com.au / website - www.strataedgesupply.example.com.au

Requirements
Must have
• Business details as per the above. The phone and fax numbers will be confirmed before the end of the project. Thank you
• SINGLE SIDED ONLY please on Card, not transparent plastic

```html
<!DOCTYPE html>
<html lang="en">
<head>
<meta charset="utf-8">
<title>Strata Edge Supply – Business Card</title>
<link rel="stylesheet" href="https://fonts.googleapis.com/css2?family=Source+Sans+3:wght@400;600;700&display=swap">
<style>
  :root {
    --brand-blue: #0d9bd8;
    --brand-grey: #58595b;
    --ink: #2a2a2a;
    --card: #ffffff;
    --backdrop-top: #2b2b2b;
    --backdrop-bottom: #050505;
  }
  * { margin: 0; padding: 0; box-sizing: border-box; }
  html, body { width: 1200px; height: 900px; overflow: hidden; }
  body {
    position: relative;
    background: linear-gradient(180deg, var(--backdrop-top) 0%, #161616 50%, var(--backdrop-bottom) 100%);
    font-family: "Source Sans 3", "Myriad Pro", Arial, sans-serif;
    color: var(--ink);
  }
  .card {
    position: absolute;
    left: 423px; top: 170px;
    width: 347px; height: 561px;
    background: var(--card);
    text-align: center;
  }
  .accent-bar {
    position: absolute;
    left: 102px;
    width: 143px;
    background: var(--brand-blue);
  }
  .accent-bar--top { top: 0; height: 30px; }
  .accent-bar--bottom { bottom: 0; height: 28px; }

  .brand {
    position: absolute;
    top: 112px; left: 0; right: 0;
    display: flex; align-items: center; justify-content: center; gap: 10px;
  }
  .brand__mark {
    width: 16px; height: 16px;
    background: var(--brand-blue);
  }
  .brand__name {
    font-weight: 700;
    font-size: 26px;
    letter-spacing: 0.5px;
    color: var(--brand-grey);
    text-transform: uppercase;
    line-height: 1;
  }

  .person { position: absolute; top: 218px; left: 0; right: 0; }
  .person__name {
    font-weight: 700;
    font-size: 20px;
    color: var(--brand-blue);
    text-transform: uppercase;
    letter-spacing: 0.2px;
    line-height: 26px;
  }
  .person__title { font-size: 15.5px; line-height: 22px; }

  .contacts {
    position: absolute; top: 291px; left: 0; right: 0;
    list-style: none;
    font-size: 15.5px;
  }
  .contacts li {
    height: 23.3px;
    display: flex; align-items: center; justify-content: center; gap: 7px;
  }
  .contacts svg { width: 12px; height: 12px; fill: var(--brand-blue); flex: none; }

  .address { position: absolute; left: 0; right: 0; font-style: normal; font-size: 15.5px; line-height: 20.5px; }
  .address--street { top: 431px; }
  .address--postal { top: 479px; }
</style>
</head>
<body>
  <article class="card">
    <div class="accent-bar accent-bar--top"></div>

    <header class="brand">
      <span class="brand__mark"></span>
      <span class="brand__name">Strata Edge Supply</span>
    </header>

    <section class="person">
      <h1 class="person__name">Lewis Trenholm</h1>
      <p class="person__title">Managing Director</p>
    </section>

    <ul class="contacts">
      <li>
        <svg viewBox="0 0 12 12" aria-hidden="true"><path d="M3.5 0h5A1 1 0 0 1 9.5 1v10a1 1 0 0 1-1 1h-5a1 1 0 0 1-1-1V1a1 1 0 0 1 1-1zm.3 1.3v8.2h4.4V1.3zM6 10.2a.6.6 0 1 0 0 1.2.6.6 0 0 0 0-1.2z"/></svg>
        <span>0427 195 864</span>
      </li>
      <li>
        <svg viewBox="0 0 12 12" aria-hidden="true"><path d="M0 4c0-2 2.5-2.5 6-2.5S12 2 12 4v1H9V3.8H3V5H0zM2.5 5.5h7L11 11H1zM6 6.6a1.6 1.6 0 1 0 0 3.2 1.6 1.6 0 0 0 0-3.2z"/></svg>
        <span>07 5571 9346</span>
      </li>
      <li>
        <svg viewBox="0 0 12 12" aria-hidden="true"><path d="M3 0h5l2 2v3h1a1 1 0 0 1 1 1v6H0V6a1 1 0 0 1 1-1h2zm1 1v4h5V2.5H7.5V1zM1.2 7v4h1.6V7zm3.8.2v1h1v-1zm2 0v1h1v-1zm2 0v1h1v-1zm-4 2v1h1v-1zm2 0v1h1v-1zm2 0v1h1v-1z"/></svg>
        <span>07 5571 9420</span>
      </li>
      <li>
        <svg viewBox="0 0 12 12" aria-hidden="true"><path d="M0 2h12v1L6 7 0 3zm0 2.3 6 4 6-4V10H0z"/></svg>
        <span>lt@strataedgesupply.example.com.au</span>
      </li>
      <li>
        <svg viewBox="0 0 12 12" aria-hidden="true"><path d="M7 1.2a2.6 2.6 0 0 1 3.7 3.7L9.2 6.4 8.4 5.6l1.5-1.5A1.5 1.5 0 0 0 7.8 2L6.3 3.5l-.8-.8zM4.1 8.7l4.6-4.6-.8-.8-4.6 4.6zM5 11a2.6 2.6 0 0 1-3.7-3.7l1.5-1.5.8.8-1.5 1.5A1.5 1.5 0 0 0 4.2 10.2l1.5-1.5.8.8z"/></svg>
        <span>www.strataedgesupply.example.com.au</span>
      </li>
    </ul>

    <address class="address address--street">Unit 3, 14 Kestrel Parade, Ormeau<br>4208 Queensland AU</address>
    <address class="address address--postal">PO Box 917, Oxenford<br>4210 Queensland AU</address>

    <div class="accent-bar accent-bar--bottom"></div>
  </article>
</body>
</html>
```